Business Cards, Stationery and Envelope Design
The Law Office of Gavin T. Morrell, P.A.
Professional
Gavin T. Morrell, Esq., LL.M.
Attorney at Law
2847 Heronwood Commerce Boulevard
Suite 214
Sunrise, FL 33319
gavin@gtmlegalgroup-example.com
www.gtmlegalgroup-example.com
Want logo to be on the business card, stationery and envelope. Would like to see writing in black but also a little color in the card, stationery and envelope other than just in the logo.
Business Formation & Structuring
Purchase & Sale of Business
Contract Review & Preparation
Shareholder Agreements
Loan Transactions
Tax Matters
Real Estate Closings
.ai file now uploaded
Attached is a file with my logo. Please let me know if you need it in another format.

```html
<!DOCTYPE html>
<html lang="en">
<head>
<meta charset="utf-8">
<title>Gavin T. Morrell, P.A. — Stationery Suite</title>
<link rel="stylesheet" href="https://fonts.googleapis.com/css2?family=Cormorant+Garamond:wght@600&family=Open+Sans:wght@400;600&display=swap">
<style>
  :root {
    --paper: #ffffff;
    --ground: #ffffff;
    --ink: #1d1d1d;
    --muted: #6b6b6b;
    --rule: #9a9a9a;
    --green: #2f7d3a;
    --green-dark: #1f5a29;
    --edge: #dcdcdc;
    --shadow: rgba(0,0,0,0.14);
  }
  * { box-sizing: border-box; margin: 0; padding: 0; }
  html, body { width: 1200px; height: 482px; overflow: hidden; background: var(--ground); }
  body { position: relative; font-family: "Open Sans", Arial, sans-serif; color: var(--ink); }

  .sheet {
    position: absolute; background: var(--paper);
    border: 1px solid var(--edge); box-shadow: 2px 3px 6px var(--shadow);
  }

  .brand { display: flex; align-items: center; gap: 5px; }
  .brand-mark { width: 16px; height: 16px; background: var(--green); flex: none; }
  .brand-name {
    font-family: "Cormorant Garamond", Georgia, serif; font-weight: 600;
    font-size: 9px; letter-spacing: .4px; text-transform: uppercase; color: var(--ink); line-height: 1.1;
  }

  .footer { position: absolute; left: 0; right: 0; text-align: center; font-size: 4.6px; color: var(--muted); line-height: 1.5; }
  .footer-rule { position: absolute; left: 14px; right: 14px; height: 1px; background: var(--rule); }
  .footer-rule::after { content: ""; position: absolute; right: 0; top: -1px; width: 34%; height: 3px; background: var(--green); }

  /* Fax cover */
  .fax { left: 24px; top: 29px; width: 276px; height: 411px; }
  .fax .brand { position: absolute; top: 22px; right: 22px; }
  .fax-fields { position: absolute; top: 92px; left: 30px; right: 30px; display: grid; grid-template-columns: 1fr 1fr; gap: 9px 20px; }
  .fax-field { display: flex; align-items: flex-end; gap: 6px; font-size: 6px; }
  .fax-field span { width: 24px; }
  .fax-field i { flex: 1; border-bottom: 1px solid var(--rule); height: 7px; }
  .fax-checks { position: absolute; top: 176px; left: 30px; right: 30px; display: flex; justify-content: space-between; font-size: 4.8px; }
  .fax-checks label { display: flex; align-items: center; gap: 2px; }
  .fax-checks label::before { content: ""; width: 5px; height: 5px; border: 1px solid var(--ink); }
  .fax-divider { position: absolute; top: 192px; left: 14px; right: 14px; height: 1px; background: var(--rule); }

  /* Envelopes */
  .envelope { left: 355px; width: 341px; height: 162px; }
  .envelope-front { top: 96px; }
  .envelope-front .brand { position: absolute; top: 14px; left: 16px; }
  .envelope-back { top: 300px; height: 156px; }
  .envelope-flap { position: absolute; inset: 0; }
  .envelope-back .brand-mark { position: absolute; left: 162px; top: 56px; width: 18px; height: 18px; }

  /* Letterhead */
  .letterhead { left: 792px; top: 29px; width: 276px; height: 411px; }
  .letterhead .brand { position: absolute; top: 22px; left: 50%; transform: translateX(-50%); }

  /* Business cards */
  .card { left: 996px; width: 161px; height: 79px; }
  .card-front { top: 192px; }
  .card-front .brand { position: absolute; top: 10px; right: 10px; }
  .card-front .brand-name { font-size: 6.5px; }
  .card-front .brand-mark { width: 11px; height: 11px; }
  .card-contact { position: absolute; left: 10px; bottom: 9px; font-size: 4.6px; line-height: 1.45; color: var(--muted); }
  .card-contact strong { display: block; color: var(--ink); font-size: 5.6px; font-weight: 600; }
  .card-back { top: 293px; display: flex; align-items: center; justify-content: center; }
  .card-back .brand-mark { width: 24px; height: 24px; }
  .card-back .brand-name { font-size: 9px; }

  .board-rule { position: absolute; left: 24px; right: 24px; top: 462px; height: 1px; background: var(--edge); }
</style>
</head>
<body>

  <section class="sheet fax" aria-label="Fax cover sheet">
    <div class="brand"><span class="brand-mark"></span><span class="brand-name">The Law Office of<br>Gavin T. Morrell, P.A.</span></div>
    <div class="fax-fields">
      <div class="fax-field"><span>To:</span><i></i></div>
      <div class="fax-field"><span>From:</span><i></i></div>
      <div class="fax-field"><span>Fax:</span><i></i></div>
      <div class="fax-field"><span>Pages:</span><i></i></div>
      <div class="fax-field"><span>Phone:</span><i></i></div>
      <div class="fax-field"><span>Date:</span><i></i></div>
      <div class="fax-field"><span>Re:</span><i></i></div>
      <div class="fax-field"><span>Cc:</span><i></i></div>
    </div>
    <div class="fax-checks">
      <label>Urgent</label><label>For Review</label><label>Please Comment</label><label>Please Reply</label><label>Please Recycle</label>
    </div>
    <div class="fax-divider"></div>
    <div class="footer-rule" style="top:370px"></div>
    <p class="footer" style="top:376px">2847 Heronwood Commerce Boulevard | Suite 214 | Sunrise, FL 33319<br>Phone 954-555-0187 | Fax 954-555-0188<br>gavin@gtmlegalgroup-example.com | www.gtmlegalgroup-example.com</p>
  </section>

  <section class="sheet envelope envelope-front" aria-label="Envelope front">
    <div class="brand"><span class="brand-mark"></span><span class="brand-name">The Law Office of<br>Gavin T. Morrell, P.A.</span></div>
    <div class="footer-rule" style="top:124px"></div>
    <p class="footer" style="top:130px">2847 Heronwood Commerce Boulevard | Suite 214 | Sunrise, FL 33319<br>Phone 954-555-0187 | Fax 954-555-0188</p>
  </section>

  <section class="sheet envelope envelope-back" aria-label="Envelope back">
    <svg class="envelope-flap" viewBox="0 0 341 156" preserveAspectRatio="none">
      <polyline points="0,6 150,80 191,80 341,6" fill="none" stroke="#9a9a9a" stroke-width="1"/>
      <line x1="0" y1="156" x2="140" y2="82" stroke="#dcdcdc" stroke-width="1"/>
      <line x1="341" y1="156" x2="201" y2="82" stroke="#dcdcdc" stroke-width="1"/>
    </svg>
    <span class="brand-mark"></span>
  </section>

  <section class="sheet letterhead" aria-label="Letterhead">
    <div class="brand"><span class="brand-mark"></span><span class="brand-name">The Law Office of<br>Gavin T. Morrell, P.A.</span></div>
    <div class="footer-rule" style="top:370px"></div>
    <p class="footer" style="top:376px">2847 Heronwood Commerce Boulevard | Suite 214 | Sunrise, FL 33319<br>Phone 954-555-0187 | Fax 954-555-0188<br>gavin@gtmlegalgroup-example.com | www.gtmlegalgroup-example.com</p>
  </section>

  <section class="sheet card card-front" aria-label="Business card front">
    <div class="brand"><span class="brand-mark"></span><span class="brand-name">The Law Office of<br>Gavin T. Morrell, P.A.</span></div>
    <p class="card-contact"><strong>Gavin T. Morrell, Esq., LL.M.</strong>Attorney at Law<br>2847 Heronwood Commerce Boulevard, Suite 214<br>Sunrise, FL 33319 | 954-555-0187<br>gavin@gtmlegalgroup-example.com</p>
  </section>

  <section class="sheet card card-back" aria-label="Business card back">
    <div class="brand"><span class="brand-mark"></span><span class="brand-name">Morrell, P.A.</span></div>
  </section>

  <div class="board-rule"></div>
</body>
</html>
```